Vesit cards for web development company

We need a business card design for our company. The company develops online platforms and conducts marketing consulting. Company logo. The cards must fit in with us (a junior start UP), but they must also be professional enough to impress with investors like banks. We wish you a combination of classic and modern design

Target Market(s)

Business partners and IT and marketing customers

Industry/Entity Type

It Company

Contact Information for Business Card

Folgende Information müssen Drauf.
Name, Position, Telefon Nr., Mobile Nr., E-Mail adresse, Optional sind noch Webadresse und HRB Nummer

Colors

Designer to choose colors to be used in the design.

Requirements
Must have
• The cards have to fit into the logo later and have to be dynamic and serious at the same time

```html
<!DOCTYPE html>
<html lang="en">
<head>
<meta charset="utf-8">
<title>Kovo Development — Business Cards</title>
<link href="https://fonts.googleapis.com/css2?family=Montserrat:wght@500;600;700&family=Lato:wght@400;700&display=swap" rel="stylesheet">
<style>
  :root {
    --stage: #202022;
    --card: #161617;
    --card-pattern-a: #1d1d1f;
    --card-pattern-b: #242426;
    --brand-blue: #2a7bc8;
    --ink-white: #f2f2f2;
    --ink-grey: #9a9a9c;
    --ink-soft: #d8d8d8;
  }
  * { margin: 0; padding: 0; box-sizing: border-box; }
  html, body {
    width: 1200px; height: 1200px; overflow: hidden;
    background: var(--stage);
  }
  .stage {
    width: 1200px; height: 1200px;
    display: flex; flex-direction: column; align-items: center; justify-content: center;
    gap: 40px;
  }
  .card {
    width: 860px; height: 491px;
    position: relative;
    background: var(--card);
    box-shadow: 0 18px 40px rgba(0,0,0,.55);
    overflow: hidden;
  }
  .card-front__texture {
    position: absolute; inset: 0;
    background: linear-gradient(135deg, var(--card-pattern-b), var(--card-pattern-a));
  }
  .wordmark {
    position: absolute;
    font-family: "Montserrat", sans-serif;
    font-weight: 700;
    color: var(--brand-blue);
    letter-spacing: 2px;
    text-align: center;
    line-height: 1.05;
  }
  .card-front .wordmark {
    left: 0; right: 0; top: 50%; transform: translateY(-50%);
    font-size: 58px;
  }
  .card-back .wordmark {
    right: 60px; top: 170px;
    font-size: 44px;
    text-align: right;
  }
  .wordmark__line { display: block; }
  .person {
    position: absolute; left: 70px; top: 62px;
    font-family: "Montserrat", sans-serif;
  }
  .person__name {
    color: var(--ink-white); font-weight: 700; font-size: 28px; letter-spacing: .5px;
  }
  .person__role {
    color: var(--ink-grey); font-weight: 600; font-size: 18px; letter-spacing: .5px; margin-top: 2px;
  }
  .contacts {
    position: absolute; left: 70px; bottom: 58px;
    list-style: none;
    font-family: "Lato", sans-serif; font-size: 23px; color: var(--ink-white);
  }
  .contacts li { display: flex; align-items: center; gap: 16px; height: 34px; }
  .contacts svg { width: 24px; height: 24px; fill: var(--brand-blue); flex: none; }
  .address {
    position: absolute; right: 70px; bottom: 120px;
    font-family: "Lato", sans-serif; font-size: 23px; line-height: 1.4;
    color: var(--ink-white); text-align: right;
  }
  .registry {
    position: absolute; right: 70px; bottom: 52px;
    font-family: "Lato", sans-serif; font-size: 23px; color: var(--ink-grey);
  }
</style>
</head>
<body>
<main class="stage">
  <section class="card card-front">
    <div class="card-front__texture" role="img" aria-label="Faint repeating brand pattern across the card face"></div>
    <div class="wordmark">
      <span class="wordmark__line">KOVO</span>
      <span class="wordmark__line">DEVELOPMENT</span>
    </div>
  </section>

  <section class="card card-back">
    <div class="person">
      <p class="person__name">MARCUS HALE</p>
      <p class="person__role">MANAGING DIRECTOR</p>
    </div>

    <div class="wordmark">
      <span class="wordmark__line">KOVO</span>
      <span class="wordmark__line">DEVELOPMENT</span>
    </div>

    <ul class="contacts">
      <li>
        <svg viewBox="0 0 24 24" aria-hidden="true"><path d="M3 8c0-2 2-4 9-4s9 2 9 4v2h-5V8H8v2H3zM6 11h12l2 9H4z"/></svg>
        <span>+61(8) 5550 2817</span>
      </li>
      <li>
        <svg viewBox="0 0 24 24" aria-hidden="true"><path d="M7 1h10a1 1 0 0 1 1 1v20a1 1 0 0 1-1 1H7a1 1 0 0 1-1-1V2a1 1 0 0 1 1-1zm1 3v12h8V4zm4 14a1.5 1.5 0 1 0 0 3 1.5 1.5 0 0 0 0-3z"/></svg>
        <span>+61(400) 555 372</span>
      </li>
      <li>
        <svg viewBox="0 0 24 24" aria-hidden="true"><path d="M2 5h20v14H2zm2 2v.5l8 5.5 8-5.5V7zm0 3v7h16v-7l-8 5.5z"/></svg>
        <span>marcushale@brightloop.com</span>
      </li>
      <li>
        <svg viewBox="0 0 24 24" aria-hidden="true"><path d="M12 2a10 10 0 1 0 0 20 10 10 0 0 0 0-20zm0 2a8 8 0 0 1 7.7 6H15a12 12 0 0 0-2-5.9A8 8 0 0 0 12 4zm-1.2.1A12 12 0 0 0 9 10H4.3a8 8 0 0 1 6.5-5.9zM4.3 12H9a12 12 0 0 0 1.8 7.9A8 8 0 0 1 4.3 12zm6.7 0h2a10 10 0 0 1-1 6 10 10 0 0 1-1-6zm4 0h4.7a8 8 0 0 1-6.5 7.9A12 12 0 0 0 15 12z"/></svg>
        <span>www.brightloop.com</span>
      </li>
    </ul>

    <p class="address">Suite 7/14 Harbour Rd<br>East Perth WA 6004</p>
    <p class="registry">HRB Nummer</p>
  </section>
</main>
</body>
</html>
```